Meadowlark Learning Growth Partners (MLGP)

This is a professional business card. Logo and picture are a must on the front of the card. I am an educational consultant. I have been consulting for the past three years for a company. I am now opening my own company. My goal for my consulting company is to eventually consult all over America.

Target Market(s)

Educators, schools, professionals

Industry/Entity Type

Consulting

Contact Information for Business Card

Picture/logo on front, simple modern design

Font styles to use
Serif

Colors
85abd2
0355a3
3176b5
cedeed

Requirements
Must have
• picture, logo,
• Odessa Pruitt, Ed.S
• address 5073 Cormorant ridge Dr. Nashville, TN 37940
• Cell:616-555-0148
• Office: 629-555-0172
• www.Mlgpedu.example
• pruittodessa@mailbox.example

```html
<!DOCTYPE html>
<html lang="en">
<head>
<meta charset="utf-8">
<title>Meadowlark Learning Growth Partners – Business Card</title>
<link href="https://fonts.googleapis.com/css2?family=Roboto:wght@300;400;700&display=swap" rel="stylesheet">
<style>
  :root {
    --page-bg: #e8e9ea;
    --front-blue: #0d57a6;
    --front-faint: #0c4f97;
    --navy: #033a7a;
    --name-blue: #1155a5;
    --icon-blue: #0d57a6;
    --text-grey: #3d3d3d;
    --faint-grey: #ededed;
    --white: #ffffff;
  }
  * { margin: 0; padding: 0; box-sizing: border-box; }
  html, body {
    width: 959px; height: 1200px; overflow: hidden;
    background: var(--page-bg);
    font-family: "Roboto", Arial, sans-serif;
  }
  .canvas { position: relative; width: 959px; height: 1200px; }

  .card {
    position: absolute; overflow: hidden;
    box-shadow: 0 10px 24px rgba(0,0,0,0.18);
  }
  .card-front { left: 28px; top: 46px; width: 910px; height: 520px; background: var(--front-blue); }
  .card-back { left: 26px; top: 639px; width: 908px; height: 519px; background: var(--white); }

  .faint-ring {
    position: absolute; border-radius: 50%;
  }
  .card-front .faint-ring {
    left: 730px; top: 150px; width: 330px; height: 330px;
    background: var(--front-faint);
  }
  .card-back .faint-ring {
    left: -190px; top: 120px; width: 360px; height: 360px;
    background: var(--faint-grey);
  }

  .brand {
    position: absolute; display: flex; flex-direction: column; align-items: center;
  }
  .brand-dot { border-radius: 50%; }
  .brand-name {
    font-family: "Roboto", Arial, sans-serif; font-weight: 700;
    letter-spacing: 0.08em; line-height: 1;
  }
  .card-front .brand { left: 316px; top: 92px; width: 280px; }
  .card-front .brand-dot { width: 140px; height: 140px; background: var(--white); margin-bottom: 48px; }
  .card-front .brand-name { color: var(--white); font-size: 86px; }

  .card-back .brand { left: 120px; top: 118px; width: 250px; }
  .card-back .brand-dot { width: 120px; height: 120px; background: var(--navy); margin-bottom: 42px; }
  .card-back .brand-name { color: var(--navy); font-size: 80px; }

  .person { position: absolute; left: 472px; top: 72px; }
  .person-name { color: var(--name-blue); font-weight: 700; font-size: 32px; line-height: 38px; letter-spacing: -0.3px; }
  .person-title { color: var(--text-grey); font-weight: 300; font-size: 33px; line-height: 38px; }

  .contact-list { position: absolute; left: 0; top: 0; list-style: none; }
  .contact-item {
    position: absolute; left: 472px; display: flex; align-items: center;
    color: var(--text-grey); font-weight: 300; font-size: 24px; line-height: 30px;
    white-space: nowrap;
  }
  .contact-item svg { width: 28px; height: 28px; margin-right: 24px; flex: none; }
  .contact-address { top: 188px; }
  .contact-cell { top: 270px; }
  .contact-office { top: 315px; }
  .contact-web { top: 357px; }
  .contact-mail { top: 397px; }

  .footer-band {
    position: absolute; left: 0; bottom: 0; width: 908px; height: 26px; background: var(--navy);
  }
  .footer-slash {
    position: absolute; left: 688px; bottom: -4px; width: 5px; height: 34px;
    background: var(--white); transform: skewX(24deg);
  }
</style>
</head>
<body>
<div class="canvas">

  <section class="card card-front">
    <div class="faint-ring"></div>
    <div class="brand">
      <div class="brand-dot"></div>
      <div class="brand-name">MLGP</div>
    </div>
  </section>

  <section class="card card-back">
    <div class="faint-ring"></div>
    <div class="brand">
      <div class="brand-dot"></div>
      <div class="brand-name">MLGP</div>
    </div>

    <div class="person">
      <div class="person-name">Odessa Pruitt</div>
      <div class="person-title">Ed.S</div>
    </div>

    <ul class="contact-list">
      <li class="contact-item contact-address">
        <svg viewBox="0 0 28 28" fill="none" stroke="var(--icon-blue)" stroke-width="2.2"><path d="M14 26c-6-7-9-11-9-15a9 9 0 0 1 18 0c0 4-3 8-9 15z"/><circle cx="14" cy="11" r="3.2"/></svg>
        <span>5073 Cormorant ridge<br>Dr. Nashville, TN 37940</span>
      </li>
      <li class="contact-item contact-cell">
        <svg viewBox="0 0 28 28" fill="none" stroke="var(--icon-blue)" stroke-width="2.2"><rect x="8" y="2" width="12" height="24" rx="2"/><line x1="12" y1="22" x2="16" y2="22"/></svg>
        <span>616-555-0148</span>
      </li>
      <li class="contact-item contact-office">
        <svg viewBox="0 0 28 28" fill="var(--icon-blue)"><path d="M2 10c0-3 6-5 12-5s12 2 12 5v2h-6v-3c-4-1-8-1-12 0v3H2z"/><path d="M7 14h14l3 10H4z"/></svg>
        <span>629-555-0172</span>
      </li>
      <li class="contact-item contact-web">
        <svg viewBox="0 0 28 28" fill="none" stroke="var(--icon-blue)" stroke-width="2"><circle cx="14" cy="14" r="11"/><ellipse cx="14" cy="14" rx="5" ry="11"/><line x1="3" y1="14" x2="25" y2="14"/><line x1="5" y1="8" x2="23" y2="8"/><line x1="5" y1="20" x2="23" y2="20"/></svg>
        <span>www.Mlgpedu.example</span>
      </li>
      <li class="contact-item contact-mail">
        <svg viewBox="0 0 28 28" fill="none" stroke="var(--icon-blue)" stroke-width="2"><rect x="2" y="6" width="24" height="17"/><path d="M2 6l12 10 12-10M2 23l9-8M26 23l-9-8"/></svg>
        <span>pruittodessa@mailbox.example</span>
      </li>
    </ul>

    <div class="footer-band"></div>
    <div class="footer-slash"></div>
  </section>

</div>
</body>
</html>
```